Business card Zottelgarten

Business card is for a self-employed dog trainer with own dog school. Name and logo of the dog school are available. Color specifications as well. The design should be classy and minimalist, but also modern. An already existing idea would be: Front: Only the logo Back: Contact data

Font styles to use
Serif
Sans Serif
Other font styles liked:
• Trajan Pro

Colors
f78f20

Requirements
Must have
• Name: Margit Wendler-Rasch Title: Dipl. Dog Trainer Contain my logo Follow my font and color preferences (see files)

```html
<!DOCTYPE html>
<html lang="de">
<head>
<meta charset="utf-8">
<title>Zottelgarten – Business Card</title>
<link href="https://fonts.googleapis.com/css2?family=Cinzel:wght@400;600;700&display=swap" rel="stylesheet">
<style>
  :root{
    --brand-brown:#7b6a5c;
    --text-brown:#6c5d51;
    --accent-orange:#f78f20;
    --card-white:#ffffff;
    --stage:#e9e5e0;
  }
  *{margin:0;padding:0;box-sizing:border-box}
  html,body{width:1200px;height:1200px;overflow:hidden;background:var(--stage)}
  body{position:relative;font-family:"Cinzel",serif;color:var(--text-brown)}

  .card{position:absolute;left:147px;width:906px;height:518px;overflow:hidden}
  .card--front{top:52px;background:var(--card-white);border-radius:0 80px 0 80px}
  .card--back{top:618px;background:var(--brand-brown);border-radius:80px 0 80px 0}

  .brand-band{position:absolute;left:99px;top:0;width:262px;height:256px;background:var(--brand-brown)}
  .brand-mark{position:absolute}
  .card--front .brand-mark{left:96px;top:122px;width:268px;height:268px}
  .card--back .brand-mark{left:318px;top:84px;width:262px;height:262px}

  .wordmark{position:absolute;text-align:center;font-weight:400;line-height:1;white-space:nowrap}
  .wordmark__name{display:block;letter-spacing:.03em}
  .wordmark__url{display:block;font-size:11px;letter-spacing:.62em;margin-top:6px}
  .card--front .wordmark{left:100px;top:412px;width:260px;color:var(--brand-brown)}
  .card--front .wordmark__name{font-size:31px}
  .card--front .wordmark__url{font-size:9px;letter-spacing:.55em}
  .card--back .wordmark{left:150px;top:352px;width:606px;color:var(--card-white)}
  .card--back .wordmark__name{font-size:52px}
  .card--back .wordmark__url{font-size:14px;margin-top:8px}

  .contact{position:absolute;left:477px;top:152px;white-space:nowrap}
  .contact__name{font-size:25px;font-weight:700;color:var(--accent-orange);letter-spacing:.01em;line-height:1}
  .contact__role{font-size:21px;font-weight:600;margin-top:12px;line-height:1}
  .contact__list{list-style:none;margin-top:34px;font-size:17px;line-height:1}
  .contact__list li{display:flex;align-items:center;gap:12px;height:18px;margin-bottom:17px}
  .contact__icon{width:20px;height:18px;flex:none}
</style>
</head>
<body>

<section class="card card--front" aria-label="Front of business card">
  <div class="brand-band"></div>
  <svg class="brand-mark" viewBox="0 0 268 268" aria-hidden="true">
    <circle cx="134" cy="134" r="131" fill="none" stroke="var(--brand-brown)" stroke-width="4"/>
    <circle cx="134" cy="134" r="124" fill="var(--brand-brown)"/>
  </svg>
  <div class="wordmark">
    <span class="wordmark__name">ZOTTELGARTEN</span>
    <span class="wordmark__url">WWW.ZOTTELGARTEN.CH</span>
  </div>

  <div class="contact">
    <p class="contact__name">MARGIT WENDLER-RASCH</p>
    <p class="contact__role">Dipl. Dog Trainer</p>
    <ul class="contact__list">
      <li>Lindenweg 12, Dübendorf</li>
      <li>
        <svg class="contact__icon" viewBox="0 0 20 18" aria-hidden="true"><path fill="var(--accent-orange)" d="M4 1c1-.6 2 0 2.6 1l1.6 2.6c.4.8.2 1.6-.5 2l-1.2.8c.8 2 2.4 3.8 4.4 4.7l.9-1.1c.5-.6 1.3-.8 2-.3l2.5 1.7c.9.6 1.1 1.6.5 2.4l-1 1.2C14.6 17 12 16.8 9 14.6 5.6 12.2 3 8.4 2.6 5.2 2.4 3.4 3 1.8 4 1z"/></svg>
        044-555-0142
      </li>
      <li>
        <svg class="contact__icon" viewBox="0 0 20 18" aria-hidden="true"><rect x="0" y="2" width="20" height="14" fill="var(--accent-orange)"/><path d="M1 3l9 7 9-7M1 15l6.5-6M19 15l-6.5-6" stroke="#fff" stroke-width="1.6" fill="none"/></svg>
        INFO@ZOTTELGARTEN.CH
      </li>
    </ul>
  </div>
</section>

<section class="card card--back" aria-label="Back of business card">
  <svg class="brand-mark" viewBox="0 0 262 262" aria-hidden="true">
    <circle cx="131" cy="131" r="128" fill="none" stroke="var(--card-white)" stroke-width="4"/>
    <circle cx="131" cy="131" r="121" fill="var(--card-white)"/>
  </svg>
  <div class="wordmark">
    <span class="wordmark__name">ZOTTELGARTEN</span>
    <span class="wordmark__url">WWW.ZOTTELGARTEN.CH</span>
  </div>
</section>

</body>
</html>
```